Newlyweds banner image for wedding reception

Banner with the words “The Newlyweds” (No quotations) in an elegant and thick (bold) font. Font must be easy to read. Gold or silver letters. Words should easily be edited so that we have the option to print in gold or silver. No background. Image must have source file as well as be delivered as a png with a transparent background. Image will be printed in a horizontal orientation. Must be 300 Dpi for printing. Image must not lose any quality and remain crisp and sharp when expanded and printed to a size of up to 6 feet wide and 2 feet tall. Be creative but we are looking for an elegant option. First and foremost.

Target Market(s)

Wedding planners, brides planning wedding and reception

Industry/Entity Type

Wedding decoration

Colors

Designer to choose colors to be used in the design.

Requirements
Must have
• Gold or Silver letters
Should not have
• Do not mix colors

```html
<!DOCTYPE html>
<html lang="en">
<head>
<meta charset="UTF-8">
<title>The Newlyweds – Reception Banner</title>
<link href="https://fonts.googleapis.com/css2?family=Libre+Baskerville:ital,wght@1,700&family=Oswald:wght@600&display=swap" rel="stylesheet">
<style>
  :root {
    --page-bg: #ffffff;
    --letter-gold: #c49a2a;
    --frame-yellow: #f7ef7a;
    --wreath-light: #fbd98a;
    --wreath-deep: #f2a94a;
    --divider-gold: #c9a43a;
  }
  html, body {
    margin: 0;
    padding: 0;
    width: 1200px;
    height: 782px;
    overflow: hidden;
    background: var(--page-bg);
  }
  .banner {
    position: relative;
    width: 1200px;
    height: 782px;
  }
  .banner-art {
    position: absolute;
    left: 0;
    top: 0;
  }
  .title {
    position: absolute;
    left: 0;
    width: 1200px;
    margin: 0;
    text-align: center;
    color: var(--letter-gold);
    line-height: 1;
  }
  .title-article {
    top: 296px;
    font-family: "Libre Baskerville", "Times New Roman", serif;
    font-style: italic;
    font-weight: 700;
    font-size: 46px;
    letter-spacing: 1px;
  }
  .title-main {
    top: 344px;
    font-family: "Oswald", "Arial Narrow", sans-serif;
    font-weight: 600;
    font-size: 90px;
    letter-spacing: 1px;
    transform: scaleX(1.02);
  }
</style>
</head>
<body>
  <div class="banner">
    <svg class="banner-art" width="1200" height="782" viewBox="0 0 1200 782">
      <defs>
        <linearGradient id="wreathTone" x1="0" y1="0" x2="1" y2="1">
          <stop offset="0" stop-color="var(--wreath-deep)"/>
          <stop offset="0.5" stop-color="var(--wreath-light)"/>
          <stop offset="1" stop-color="var(--wreath-deep)"/>
        </linearGradient>
      </defs>
      <path class="floral-wreath" role="img" aria-label="Gold floral wreath of leaves, flowers and berries encircling the title"
            fill="url(#wreathTone)" fill-opacity="0.45" fill-rule="evenodd"
            d="M254,391 a346,165 0 1,0 692,0 a346,165 0 1,0 -692,0 Z
               M316,391 a284,132 0 1,0 568,0 a284,132 0 1,0 -568,0 Z"/>
      <ellipse class="oval-frame" cx="601" cy="391" rx="272" ry="130"
               fill="none" stroke="var(--frame-yellow)" stroke-width="4"/>
      <g class="title-divider" stroke="var(--divider-gold)" fill="var(--divider-gold)">
        <line x1="441" y1="464" x2="765" y2="464" stroke-width="1.5"/>
        <circle cx="540" cy="464" r="2.5"/>
        <circle cx="571" cy="464" r="2"/>
        <circle cx="601" cy="464" r="2"/>
        <circle cx="631" cy="464" r="2"/>
        <circle cx="662" cy="464" r="2.5"/>
      </g>
    </svg>
    <p class="title title-article">The</p>
    <h1 class="title title-main">NEWLYWEDS</h1>
  </div>
</body>
</html>
```